" Clínica médica que atua nas diversas especialidades e realiza atendimentos particulares a preços acessíveis, podendo futuramente atender planos de saúde. "

```html
<!DOCTYPE html>
<html lang="pt-BR">
<head>
<meta charset="utf-8">
<title>VitaMed — Clínica Médica</title>
<link href="https://fonts.googleapis.com/css2?family=Oswald:wght@400;500;600&family=Open+Sans:wght@300;400;600;700&display=swap" rel="stylesheet">
<style>
  :root{
    --backdrop:#e4e4e4;
    --white:#ffffff;
    --green-deep:#0d3f2b;
    --green-dark:#14533a;
    --green-mid:#1f7a4a;
    --green:#3aa64a;
    --green-bright:#5cc25a;
    --green-pale:#bfe6b8;
    --ink:#24453a;
    --ink-soft:#6b7f76;
  }
  *{margin:0;padding:0;box-sizing:border-box}
  html,body{width:1200px;height:1200px;overflow:hidden;background:var(--backdrop)}
  body{font-family:"Open Sans",Arial,sans-serif;position:relative}
  .page{position:absolute;left:230px;top:0;width:790px;height:1200px;background:var(--white);box-shadow:0 6px 24px rgba(0,0,0,.25);overflow:hidden}

  /* header */
  .site-header{position:absolute;left:0;top:0;width:790px;height:72px;background:var(--white);display:flex}
  .brand{width:142px;height:72px;background:var(--green-dark);display:flex;align-items:center;justify-content:center;gap:8px;color:var(--white);font-weight:600;font-size:17px}
  .brand-dot{width:12px;height:12px;border-radius:50%;background:var(--green-bright)}
  .header-main{flex:1;position:relative}
  .top-info{position:absolute;top:6px;left:20px;right:12px;display:flex;justify-content:space-between;font-size:7px;color:var(--ink-soft)}
  .main-nav{position:absolute;top:22px;left:0;right:0;height:50px;display:flex;align-items:center;justify-content:space-around;font-size:12px;color:var(--ink);text-align:center;line-height:1.15}
  .results-btn{width:154px;height:72px;background:var(--green-deep);color:var(--white);font-weight:700;font-size:11px;display:flex;align-items:center;justify-content:center;text-align:center;line-height:1.25}

  /* hero */
  .hero{position:absolute;left:0;top:72px;width:790px;height:372px;background:linear-gradient(90deg,#a6dca0 0%,#6fc46b 35%,#dff2dc 75%,#bfe3bc 100%)}
  .hero-photo{position:absolute;right:40px;top:0;width:470px;height:372px;background:radial-gradient(ellipse at 50% 55%,#f4f8f4 0%,#d8ecd6 55%,rgba(200,230,196,0) 80%)}
  .hero-title{position:absolute;left:88px;top:132px;font-family:"Oswald",sans-serif;font-weight:500;font-size:38px;line-height:1.1;color:var(--white);letter-spacing:.5px}
  .hero-arrow{position:absolute;top:228px;width:22px;height:22px;background:var(--green-deep);display:flex;align-items:center;justify-content:center}
  .hero-arrow.prev{left:8px}
  .hero-arrow.next{right:8px}
  .hero-strip{position:absolute;left:0;top:444px;width:790px;height:12px;background:linear-gradient(90deg,var(--green-mid),var(--green-bright))}

  /* services */
  .services{position:absolute;left:0;top:456px;width:389px;height:336px;background:linear-gradient(180deg,var(--green) 0%,#2f9a45 100%);padding:34px 0 0 88px;color:var(--white)}
  .services h2{font-family:"Oswald",sans-serif;font-weight:500;font-size:15px;letter-spacing:.5px;margin-bottom:10px}
  .service-cols{display:flex;gap:34px}
  .service-col ul{list-style:none;font-size:8px;line-height:21px;width:118px}
  .more-btn{display:inline-block;margin-top:10px;background:var(--green-deep);font-size:7px;font-weight:700;padding:3px 10px}

  .promo{position:absolute;left:389px;top:456px;width:401px;height:166px;background:var(--white)}
  .promo-text{position:absolute;left:22px;top:36px;font-family:"Oswald",sans-serif;font-weight:500;font-size:17px;line-height:1.15;color:var(--green-dark)}
  .promo-brand{position:absolute;left:22px;top:128px;display:flex;align-items:center;gap:4px;font-size:8px;font-weight:600;color:var(--green-mid)}
  .promo-brand i{width:8px;height:8px;background:var(--green-mid);display:block}
  .promo-photo{position:absolute;right:0;top:0;width:230px;height:166px;background:radial-gradient(ellipse at 60% 55%,#d9c2ae 0%,#eadfd5 45%,#ffffff 78%)}

  .card{position:absolute;top:622px;height:170px;padding:16px 14px}
  .card.guide{left:389px;width:178px;background:linear-gradient(180deg,#eef6ee,#e2efe2)}
  .card.collect{left:567px;width:223px;background:linear-gradient(180deg,#d7e9d7,#c3dcc4)}
  .card-title{font-weight:300;font-size:21px;line-height:1.1;color:var(--green-dark);padding-bottom:8px;border-bottom:2px solid var(--green)}
  .card-link{margin-top:6px;font-size:13px;color:var(--green-dark);display:flex;align-items:center;gap:8px}
  .card-text{margin-top:8px;font-size:13px;line-height:1.25;color:var(--green-dark)}

  .responsible{position:absolute;left:0;top:792px;width:790px;height:60px;background:var(--green-dark);color:#d5eadb;font-size:10px;display:flex;align-items:center;justify-content:center}

  /* footer */
  .site-footer{position:absolute;left:0;top:852px;width:790px;height:348px;background:linear-gradient(180deg,#123f2d,#0c3224);color:var(--white)}
  .footer-col{position:absolute;top:24px}
  .footer-col h3{font-family:"Oswald",sans-serif;font-weight:500;font-size:22px;letter-spacing:.5px;padding-bottom:8px;border-bottom:1px solid rgba(255,255,255,.5);margin-bottom:12px}
  .clinic{left:88px;width:130px}
  .clinic p{font-size:10px;line-height:14px;color:#dfeee4}
  .clinic strong{font-size:13px;display:block;margin-bottom:2px}
  .sitemap{left:308px;width:240px}
  .sitemap ul{list-style:none;display:grid;grid-template-columns:100px 120px;row-gap:16px;font-size:10px;color:#dfeee4}
  .social{left:600px;width:110px}
  .social h3{border:none;line-height:1;font-size:22px}
  .social h3 span{display:block;font-weight:400}
  .social-icons{display:flex;gap:6px;margin-top:-2px}
  .social-icons i{width:16px;height:16px;background:var(--white);border-radius:3px;display:block}
</style>
</head>
<body>
<div class="page">
  <header class="site-header">
    <div class="brand"><span class="brand-dot"></span>VitaMed</div>
    <div class="header-main">
      <div class="top-info"><span>Rua Seu Endereço, 00 · Centro</span><span>(48) 0000-0000</span></div>
      <nav class="main-nav">
        <span>Quem Somos</span>
        <span>Consultas<br>e Tratamentos</span>
        <span>Exames</span>
        <span>Fale Conosco</span>
      </nav>
    </div>
    <div class="results-btn">RESULTADOS<br>DE EXAMES</div>
  </header>

  <section class="hero">
    <div class="hero-photo" role="img" aria-label="Fotografia da equipe médica de jaleco branco"></div>
    <h1 class="hero-title">VIVER BEM É<br>ESTAR BEM</h1>
    <div class="hero-arrow prev"><svg width="8" height="10" viewBox="0 0 8 10"><path d="M6 1 2 5l4 4" fill="none" stroke="#fff" stroke-width="2"/></svg></div>
    <div class="hero-arrow next"><svg width="8" height="10" viewBox="0 0 8 10"><path d="M2 1l4 4-4 4" fill="none" stroke="#fff" stroke-width="2"/></svg></div>
  </section>
  <div class="hero-strip"></div>

  <section class="services">
    <h2>EXAMES E CONSULTAS</h2>
    <div class="service-cols">
      <div class="service-col">
        <ul>
          <li>RX / TC</li><li>Tomografia Computadorizada</li><li>Ressonância Magnética</li>
          <li>Tomossíntese</li><li>Medicina Nuclear</li><li>Raio-x Digital</li>
          <li>Mamografia Digital</li><li>Densitometria Óssea</li><li>Endoscopia Digestiva</li>
        </ul>
        <span class="more-btn">MAIS</span>
      </div>
      <div class="service-col">
        <ul>
          <li>Cardiologia</li><li>Clínica Médica (clínico geral)</li><li>Dermatologia</li>
          <li>Endocrinologia</li><li>Gastroenterologia</li><li>Ginecologia</li>
          <li>Neurocirurgia</li><li>Neurologia</li><li>Nutrição</li>
        </ul>
        <span class="more-btn">MAIS</span>
      </div>
    </div>
  </section>

  <section class="promo">
    <div class="promo-photo" role="img" aria-label="Fotografia de uma família sorridente"></div>
    <p class="promo-text">RESULTADOS<br>RÁPIDOS.<br>CREDIBILIDADE<br>LONGA.</p>
    <div class="promo-brand"><i></i>VitaMed</div>
  </section>

  <article class="card guide">
    <p class="card-title">Orientações<br>de Exames</p>
    <p class="card-link">Saiba mais <svg width="22" height="8" viewBox="0 0 22 8"><path d="M0 4h20M16 1l4 3-4 3" fill="none" stroke="#14533a" stroke-width="1.4"/></svg></p>
  </article>
  <article class="card collect" role="img" aria-label="Fotografia de coleta de exame ao fundo">
    <p class="card-title">Coleta<br>Externa</p>
    <p class="card-text">Faça o<br>agendamento<br>de sua Coleta</p>
  </article>

  <div class="responsible">Responsável técnico Dr. Nome e Sobrenome - CRM - 00000</div>

  <footer class="site-footer">
    <div class="footer-col clinic">
      <h3>CLÍNICA</h3>
      <p><strong>Bairro</strong>R. Seu Endereço, 00<br>CEP: 000-0000<br>(48) 0000-0000<br>(48) 0000-0000<br>Atendimento das<br>8h às 18h</p>
    </div>
    <div class="footer-col sitemap">
      <h3>MAPA DO SITE</h3>
      <ul>
        <li>Página Inicial</li><li>Quem Somos</li>
        <li>Para Cliente</li><li>Consultas</li>
        <li>Para Clínica</li><li>Tratamento</li>
        <li>Fale Conosco</li><li>Perguntas Frequentes</li>
      </ul>
    </div>
    <div class="footer-col social">
      <h3>REDES<span>SOCIAIS</span></h3>
      <div class="social-icons"><i></i><i></i></div>
    </div>
  </footer>
</div>
</body>
</html>
```